Consulting Company Business Card

I am looking for a minimalist, classy, professional design on my business card. I would like it to be double-sided. I want to use the font and color scheme of my logo which are attached. Please be creative in the designs that you send me. I want to play off the design of my logo with the inner C that is Green and Blue broken up with the white.
Target Market(s)
Small Businesses
Industry/Entity Type
Consulting
Contact Information for Business Card
Dale M. Whitcombe, CPA CGMA, 555-014-2873, dwhitcombe@vorantaadvisory.example, www.vorantaadvisory.example

```html
<!DOCTYPE html>
<html lang="en">
<head>
<meta charset="utf-8">
<title>Voranta Advisory – Business Card</title>
<link rel="stylesheet" href="https://fonts.googleapis.com/css2?family=Montserrat:wght@500;700&family=Arimo:wght@400&display=swap">
<style>
  :root {
    --navy: #213159;
    --teal: #1e8280;
    --white: #ffffff;
    --backdrop: #2a2a2c;
  }
  * { margin: 0; padding: 0; box-sizing: border-box; }
  html, body { width: 1200px; height: 1015px; overflow: hidden; }
  body {
    background: var(--backdrop);
    position: relative;
    font-family: "Montserrat", sans-serif;
  }
  .card {
    position: absolute;
    width: 540px;
    height: 309px;
    overflow: hidden;
    box-shadow: 0 14px 30px rgba(0,0,0,.45);
  }
  .card--front {
    left: 50px; top: 190px;
    background: linear-gradient(180deg, var(--teal) 0%, #1f5a6e 50%, var(--navy) 85%);
    display: flex; align-items: center; justify-content: center;
  }
  .brand-name {
    font-family: "Montserrat", sans-serif;
    font-weight: 700;
    letter-spacing: .06em;
    text-transform: uppercase;
    white-space: nowrap;
  }
  .card--front .brand-name { color: var(--white); font-size: 34px; }
  .card--back { left: 610px; top: 510px; background: var(--navy); }
  .back-art { position: absolute; inset: 0; }
  .card--back .brand-name {
    position: absolute; left: 420px; top: 120px;
    transform: translate(-50%, -50%);
    color: var(--navy); font-size: 17px;
  }
  .holder { position: absolute; left: 36px; top: 68px; color: var(--white); }
  .holder__name { font-weight: 700; font-size: 17px; letter-spacing: .03em; text-transform: uppercase; white-space: nowrap; }
  .holder__title { font-family: "Arimo", sans-serif; font-size: 13px; margin-top: 4px; }
  .contact {
    position: absolute; left: 36px; bottom: 24px;
    list-style: none; color: var(--white);
    font-family: "Arimo", sans-serif; font-size: 11.5px;
  }
  .contact li { display: flex; align-items: center; gap: 7px; line-height: 19px; white-space: nowrap; }
  .contact svg { width: 12px; height: 12px; flex: none; }
</style>
</head>
<body>
  <section class="card card--front">
    <span class="brand-name">Voranta Advisory</span>
  </section>

  <section class="card card--back">
    <svg class="back-art" viewBox="0 0 540 309" aria-hidden="true">
      <circle cx="406" cy="133" r="156" fill="var(--teal)" stroke="var(--white)" stroke-width="3"/>
      <circle cx="420" cy="120" r="150" fill="var(--white)"/>
    </svg>
    <span class="brand-name">Voranta Advisory</span>

    <div class="holder">
      <div class="holder__name">Dale M. Whitcombe</div>
      <div class="holder__title">CPA CGMA</div>
    </div>

    <ul class="contact">
      <li>
        <svg viewBox="0 0 24 24" fill="none" stroke="currentColor" stroke-width="2.2"><path d="M5 3h4l2 5-3 2a12 12 0 0 0 6 6l2-3 5 2v4a2 2 0 0 1-2 2A18 18 0 0 1 3 5a2 2 0 0 1 2-2z"/></svg>
        555-014-2873
      </li>
      <li>
        <svg viewBox="0 0 24 24" fill="none" stroke="currentColor" stroke-width="2"><circle cx="12" cy="12" r="10"/><path d="M2 12h20M12 2c3 3 3 17 0 20M12 2c-3 3-3 17 0 20"/></svg>
        www.vorantaadvisory.example
      </li>
      <li>
        <svg viewBox="0 0 24 24" fill="none" stroke="currentColor" stroke-width="2"><rect x="2" y="5" width="20" height="14"/><path d="M2 5l10 8 10-8"/></svg>
        dwhitcombe@vorantaadvisory.example
      </li>
    </ul>
  </section>
</body>
</html>
```